Tech business card design

We need an amazing business card design for our new business 'Brakka' a marketing tech startup based in Sydney, Australia. We provide an online marketplace for businesses to search and buy advertising media, connect with service providers and learn more about marketing. We wish to communicate 'cool tech', reliability and professionalism and design based around our logo.

Target Market(s)

Business Owners

Contact Information for Business Card

Name
Position
Email Address
Website
Phone Number

Font styles to use
Other font styles liked:
• Avenir & Avenir Next

Colors

Designer to choose colors to be used in the design.

```html
<!DOCTYPE html>
<html lang="en">
<head>
<meta charset="utf-8">
<title>Brakka Business Card</title>
<link rel="stylesheet" href="https://fonts.googleapis.com/css2?family=Montserrat:wght@500;600;700;800&display=swap">
<style>
  :root {
    --ink: #231e1f;
    --paper: #f6f3f2;
    --red: #e8373b;
    --red-deep: #b81e24;
    --white: #ffffff;
    --text: #3a3536;
    --canvas: #ffffff;
  }
  * { margin: 0; padding: 0; box-sizing: border-box; }
  html, body {
    width: 995px; height: 1200px; overflow: hidden;
    background: var(--canvas);
    font-family: "Montserrat", "Helvetica Neue", Arial, sans-serif;
  }
  .sheet { position: relative; width: 995px; height: 1200px; }
  .card {
    position: absolute; left: 43px; width: 904px; height: 540px;
    overflow: hidden; background: var(--ink);
  }
  .card--front { top: 48px; }
  .card--back { top: 620px; }
  .card__art { position: absolute; inset: 0; width: 100%; height: 100%; }
  .brand {
    position: absolute; color: var(--white);
    font-weight: 800; letter-spacing: 0.5px; line-height: 1;
  }
  .card--front .brand { left: 95px; top: 225px; font-size: 44px; }
  .card--back .brand { left: 0; right: 0; top: 236px; text-align: center; font-size: 48px; }
  .site {
    position: absolute; left: 32px; bottom: 20px;
    color: var(--white); font-size: 15px; font-weight: 700;
  }
  .identity {
    position: absolute; left: 525px; width: 265px; top: 122px;
    text-align: center; color: var(--ink);
  }
  .identity__name { font-size: 33px; font-weight: 700; line-height: 1.2; }
  .identity__role { font-size: 17px; font-weight: 600; margin-top: 2px; }
  .identity__rule {
    display: flex; margin-top: 10px; height: 3px;
  }
  .identity__rule span:first-child { width: 65px; background: var(--red); }
  .identity__rule span:last-child { flex: 1; background: var(--ink); margin-left: 4px; }
  .contacts { position: absolute; left: 522px; top: 238px; list-style: none; }
  .contacts li {
    display: flex; align-items: center; gap: 18px;
    color: var(--text); font-size: 17px; font-weight: 500; line-height: 1.35;
    margin-bottom: 27px;
  }
  .contacts svg { width: 22px; height: 22px; flex: none; fill: var(--red); }
</style>
</head>
<body>
<main class="sheet">

  <section class="card card--front">
    <svg class="card__art" viewBox="0 0 904 540" preserveAspectRatio="none" aria-hidden="true">
      <defs>
        <filter id="soft-shadow" x="-20%" y="-20%" width="140%" height="140%">
          <feGaussianBlur stdDeviation="9"/>
        </filter>
        <linearGradient id="band-front" x1="0" y1="0" x2="1" y2="1">
          <stop offset="0" stop-color="#f04446"/>
          <stop offset="1" stop-color="#c9252a"/>
        </linearGradient>
      </defs>
      <polygon points="430,0 904,0 904,540 520,540" fill="#000" opacity="0.45" filter="url(#soft-shadow)"/>
      <polygon points="345,0 430,0 520,540 448,540" fill="url(#band-front)"/>
      <polygon points="385,0 430,0 520,540 490,540" fill="var(--red-deep)" opacity="0.55"/>
      <polygon points="440,0 904,0 904,540 525,540" fill="var(--paper)"/>
    </svg>

    <div class="brand">Brakka</div>
    <div class="site">brakkamedia.com</div>

    <div class="identity">
      <div class="identity__name">Your Name</div>
      <div class="identity__role">Designation</div>
      <div class="identity__rule"><span></span><span></span></div>
    </div>

    <ul class="contacts">
      <li>
        <svg viewBox="0 0 24 24" aria-hidden="true"><path d="M12 2a7 7 0 0 0-7 7c0 5.2 7 13 7 13s7-7.8 7-13a7 7 0 0 0-7-7zm0 9.6A2.6 2.6 0 1 1 12 6.4a2.6 2.6 0 0 1 0 5.2z"/></svg>
        <span>Your Street Address Here<br>Street address 123</span>
      </li>
      <li>
        <svg viewBox="0 0 24 24" aria-hidden="true"><path d="M6.6 10.8a15.1 15.1 0 0 0 6.6 6.6l2.2-2.2a1 1 0 0 1 1-.25 11.4 11.4 0 0 0 3.6.57 1 1 0 0 1 1 1V20a1 1 0 0 1-1 1A17 17 0 0 1 3 4a1 1 0 0 1 1-1h3.5a1 1 0 0 1 1 1c0 1.25.2 2.45.57 3.57a1 1 0 0 1-.25 1z"/></svg>
        <span>+012 1256 45624<br>+012 1256 45624</span>
      </li>
      <li>
        <svg viewBox="0 0 24 24" aria-hidden="true"><path d="M12 2a10 10 0 1 0 0 20 10 10 0 0 0 0-20zm6.9 6h-2.9a15.6 15.6 0 0 0-1.4-3.6A8 8 0 0 1 18.9 8zM12 4a14 14 0 0 1 1.9 4h-3.8A14 14 0 0 1 12 4zM4.3 14a8.2 8.2 0 0 1 0-4h3.4a16.5 16.5 0 0 0 0 4zm.8 2h2.9a15.6 15.6 0 0 0 1.4 3.6A8 8 0 0 1 5.1 16zM8 8H5.1a8 8 0 0 1 4.3-3.6A15.6 15.6 0 0 0 8 8zm4 12a14 14 0 0 1-1.9-4h3.8A14 14 0 0 1 12 20zm2.3-6H9.7a14.7 14.7 0 0 1 0-4h4.6a14.7 14.7 0 0 1 0 4zm.3 5.6A15.6 15.6 0 0 0 16 16h2.9a8 8 0 0 1-4.3 3.6zm1.7-5.6a16.5 16.5 0 0 0 0-4h3.4a8.2 8.2 0 0 1 0 4z"/></svg>
        <span>Email address@email.com<br>www.website.com</span>
      </li>
    </ul>
  </section>

  <section class="card card--back">
    <svg class="card__art" viewBox="0 0 904 540" preserveAspectRatio="none" aria-hidden="true">
      <defs>
        <filter id="glow" x="-30%" y="-30%" width="160%" height="160%">
          <feGaussianBlur stdDeviation="10"/>
        </filter>
        <linearGradient id="band-back" x1="0" y1="0" x2="1" y2="1">
          <stop offset="0" stop-color="#f04446"/>
          <stop offset="1" stop-color="#c9252a"/>
        </linearGradient>
      </defs>
      <polygon points="195,0 300,0 0,420 0,290" fill="var(--red)" opacity="0.6" filter="url(#glow)"/>
      <polygon points="195,0 300,0 0,420 0,290" fill="url(#band-back)"/>
      <polygon points="240,0 300,0 0,420 0,360" fill="var(--red-deep)" opacity="0.5"/>
      <polygon points="904,150 904,250 750,540 640,540" fill="var(--red)" opacity="0.6" filter="url(#glow)"/>
      <polygon points="904,150 904,250 750,540 640,540" fill="url(#band-back)"/>
      <polygon points="904,150 904,200 700,540 640,540" fill="var(--red-deep)" opacity="0.5"/>
    </svg>

    <div class="brand">Brakka</div>
    <div class="site">brakkamedia.com</div>
  </section>

</main>
</body>
</html>
```